Bref créative
Business cards and stationary for MovRAX
Gestión Estratégica en Telecomunicaciones
I need double sided standard sized Business Card [3.5" x 2"]
We like Helvetica neue
Professional
Tomás Quevedo Arrieta
Gerente General
Calle 18 # 41-53, Bogotá, Colombia
dpalomo@movrax-ejemplo.com.co
www.movrax-ejemplo.com.co
Stationary is needed in letter sized paper, not A4.
The back of the business cards should only include the logo, and maybe the website. No other information.
This is the logo file. Note there are several versions of the logo.

```html
<!DOCTYPE html>
<html lang="es">
<head>
<meta charset="utf-8">
<title>MovRAX – Stationery</title>
<link href="https://fonts.googleapis.com/css2?family=Inter:wght@400;600;700&display=swap" rel="stylesheet">
<style>
:root{
  --stage:#2c2d2f;
  --navy:#0f2b45;
  --blue:#1c5d8c;
  --teal:#2b93b8;
  --green:#8cbb3b;
  --paper:#ffffff;
  --paper-shade:#eef1f3;
  --ink:#2a3a48;
  --label:#8d9196;
  --faint:#e6eef2;
}
*{margin:0;padding:0;box-sizing:border-box}
html,body{width:1200px;height:350px;overflow:hidden;background:var(--stage);font-family:"Inter","Helvetica Neue",Arial,sans-serif}
.sheet{position:relative;width:1200px;height:350px}
.item{position:absolute}
.label{position:absolute;font-size:6px;color:var(--label);white-space:nowrap}
.wordmark{display:flex;align-items:center;gap:3px;font-weight:700;color:var(--blue);white-space:nowrap}
.wordmark .dot{width:.8em;height:.8em;border-radius:50%;background:var(--green);flex:none}
.wordmark.on-dark{color:var(--paper)}
.concept{left:20px;top:76px;width:120px}
.concept .wordmark{font-size:19px;color:var(--teal)}
.concept .tag{font-size:4.6px;color:#b9c3cb;margin-top:3px;white-space:nowrap}
.card{position:absolute;width:95px;height:54px;overflow:hidden;box-shadow:0 2px 4px rgba(0,0,0,.4)}
.card svg{position:absolute;inset:0}
.card .wordmark{position:absolute;font-size:11px}
.card .centered{left:50%;top:50%;transform:translate(-50%,-50%)}
.card .web{position:absolute;bottom:5px;width:100%;text-align:center;font-size:3.5px;white-space:nowrap}
.card .details{position:absolute;left:7px;top:22px;font-size:3.2px;line-height:1.45;color:var(--ink);white-space:nowrap}
.card .details b{font-size:4.2px;color:var(--blue)}
.card.dark{background:var(--navy)}
.card.blue{background:linear-gradient(135deg,var(--teal),var(--blue))}
.card.white{background:var(--paper)}
.card.green{background:var(--green)}
.card.dark .web,.card.blue .web,.card.green .web{color:#dce6ee}
.page{position:absolute;background:var(--paper);overflow:hidden;box-shadow:0 3px 6px rgba(0,0,0,.45)}
.page .wordmark{position:absolute;font-size:12px}
.page .watermark{position:absolute;border-radius:50%;background:var(--faint)}
.page .foot{position:absolute;bottom:8px;width:100%;text-align:center;font-size:3.4px;color:#dfe9f0;white-space:nowrap}
.letterhead{left:440px;top:42px;width:195px;height:285px}
.folder{left:655px;top:24px;width:195px;height:303px;background:linear-gradient(var(--paper-shade),var(--paper) 18%)}
.envelope{position:absolute;overflow:hidden;box-shadow:0 2px 5px rgba(0,0,0,.45)}
.envelope .wordmark{position:absolute;font-size:8px}
</style>
</head>
<body>
<main class="sheet">

  <section class="item concept">
    <div class="wordmark"><span class="dot"></span>MovRAX</div>
    <div class="tag">Gestión Estratégica en Telecomunicaciones</div>
  </section>
  <span class="label" style="left:20px;top:126px">Stationery Concept</span>

  <div class="card dark" style="left:150px;top:62px">
    <div class="wordmark on-dark centered"><span class="dot"></span>MovRAX</div>
    <div class="web">www.movrax-ejemplo.com.co</div>
  </div>
  <span class="label" style="left:150px;top:119px">Card back</span>
  <div class="card blue" style="left:252px;top:62px">
    <div class="wordmark on-dark centered"><span class="dot"></span>MovRAX</div>
    <div class="web">www.movrax-ejemplo.com.co</div>
  </div>
  <span class="label" style="left:252px;top:119px">Card front</span>

  <div class="card dark" style="left:20px;top:155px;width:112px">
    <div class="wordmark on-dark centered"><span class="dot"></span>MovRAX</div>
    <div class="web">www.movrax-ejemplo.com.co</div>
  </div>
  <span class="label" style="left:20px;top:212px">Card back</span>
  <div class="card white" style="left:150px;top:155px">
    <div class="wordmark centered"><span class="dot"></span>MovRAX</div>
    <div class="web" style="color:var(--blue)">www.movrax-ejemplo.com.co</div>
  </div>
  <span class="label" style="left:150px;top:212px">Card back</span>
  <div class="card white" style="left:252px;top:155px">
    <svg viewBox="0 0 95 54" preserveAspectRatio="none"><path d="M0 46 Q48 38 95 45 L95 54 L0 54Z" fill="var(--blue)"/><path d="M0 44 Q48 36 95 42" stroke="var(--green)" stroke-width="1" fill="none"/></svg>
    <div class="wordmark" style="left:7px;top:6px;font-size:9px"><span class="dot"></span>MovRAX</div>
    <div class="details"><b>Tomás Quevedo Arrieta</b><br>Gerente General<br>Calle 18 # 41-53, Bogotá<br>dpalomo@movrax-ejemplo.com.co</div>
  </div>
  <span class="label" style="left:252px;top:212px">Card front</span>

  <div class="card green" style="left:20px;top:245px;width:112px">
    <div class="wordmark on-dark centered"><span class="dot" style="background:var(--paper)"></span>MovRAX</div>
    <div class="web">www.movrax-ejemplo.com.co</div>
  </div>
  <span class="label" style="left:20px;top:302px">Card back</span>
  <div class="card blue" style="left:150px;top:245px">
    <div class="wordmark on-dark" style="left:7px;top:6px;font-size:9px"><span class="dot"></span>MovRAX</div>
    <div class="details" style="color:#e4eef5"><b style="color:#fff">Tomás Quevedo Arrieta</b><br>Gerente General<br>Calle 18 # 41-53, Bogotá<br>dpalomo@movrax-ejemplo.com.co</div>
  </div>
  <span class="label" style="left:150px;top:302px">Card front</span>
  <div class="card white" style="left:252px;top:245px">
    <svg viewBox="0 0 95 54" preserveAspectRatio="none"><path d="M62 0 Q72 30 95 36 L95 0Z" fill="var(--teal)"/><path d="M54 0 Q66 32 95 40" stroke="var(--green)" stroke-width="1.2" fill="none"/></svg>
    <div class="wordmark" style="left:7px;top:6px;font-size:9px"><span class="dot"></span>MovRAX</div>
    <div class="details"><b>Tomás Quevedo Arrieta</b><br>Gerente General<br>Calle 18 # 41-53, Bogotá<br>www.movrax-ejemplo.com.co</div>
  </div>
  <span class="label" style="left:252px;top:302px">Card front</span>

  <article class="page letterhead">
    <div class="wordmark" style="left:14px;top:12px"><span class="dot"></span>MovRAX</div>
    <div class="watermark" style="left:40px;top:90px;width:110px;height:110px"></div>
    <svg style="position:absolute;left:0;bottom:0" width="195" height="34" viewBox="0 0 195 34" preserveAspectRatio="none"><path d="M0 14 Q100 0 195 10 L195 34 L0 34Z" fill="var(--blue)"/><path d="M0 12 Q100 -2 195 7" stroke="var(--green)" stroke-width="1.5" fill="none"/></svg>
    <div class="foot">Calle 18 # 41-53, Bogotá, Colombia · www.movrax-ejemplo.com.co</div>
  </article>
  <span class="label" style="left:440px;top:331px">Letterhead</span>

  <article class="page folder">
    <svg style="position:absolute;left:0;top:0" width="195" height="60" viewBox="0 0 195 60"><path d="M0 0 L97 48 L195 0" stroke="#d6dde2" stroke-width="1" fill="none"/></svg>
    <div class="wordmark" style="left:72px;top:58px;font-size:10px"><span class="dot"></span>MovRAX</div>
    <div class="watermark" style="left:45px;top:120px;width:105px;height:105px"></div>
    <svg style="position:absolute;left:0;bottom:0" width="195" height="34" viewBox="0 0 195 34" preserveAspectRatio="none"><path d="M0 14 Q100 0 195 10 L195 34 L0 34Z" fill="var(--blue)"/><path d="M0 12 Q100 -2 195 7" stroke="var(--green)" stroke-width="1.5" fill="none"/></svg>
    <div class="foot">Calle 18 # 41-53, Bogotá, Colombia · www.movrax-ejemplo.com.co</div>
  </article>
  <span class="label" style="left:655px;top:331px">Envelope</span>

  <div class="envelope" style="left:918px;top:72px;width:262px;height:98px;background:var(--paper)">
    <svg style="position:absolute;inset:0" width="262" height="98" viewBox="0 0 262 98"><rect width="262" height="30" fill="var(--green)"/><path d="M0 30 Q130 18 262 30" fill="var(--paper)"/></svg>
  </div>
  <div class="envelope" style="left:952px;top:158px;width:228px;height:62px;background:var(--paper)">
    <svg style="position:absolute;inset:0" width="228" height="62" viewBox="0 0 228 62"><path d="M0 0 L114 26 L228 0Z" fill="var(--blue)"/><path d="M0 0 L114 26 L228 0" stroke="var(--teal)" stroke-width="1" fill="none"/></svg>
    <div class="wordmark" style="left:100px;top:32px"><span class="dot"></span>MovRAX</div>
  </div>
  <div class="envelope" style="left:920px;top:200px;width:240px;height:66px;background:var(--paper)">
    <svg style="position:absolute;inset:0" width="240" height="66" viewBox="0 0 240 66"><path d="M0 0 L120 30 L240 0" stroke="#d3dbe1" stroke-width="1" fill="none"/></svg>
  </div>
  <div class="envelope" style="left:905px;top:245px;width:262px;height:78px;background:var(--paper)">
    <svg style="position:absolute;inset:0" width="262" height="78" viewBox="0 0 262 78" preserveAspectRatio="none"><path d="M0 62 Q130 50 262 60 L262 78 L0 78Z" fill="var(--blue)"/><path d="M0 60 Q130 48 262 57" stroke="var(--green)" stroke-width="1.3" fill="none"/></svg>
    <div class="wordmark" style="left:10px;top:8px"><span class="dot"></span>MovRAX</div>
  </div>
  <span class="label" style="left:1120px;top:331px">Envelope set</span>

</main>
</body>
</html>
```